Young, dynamic furniture company needs a new business card design

We require a new business card design for our modern furniture company which supplies furniture and appliances to the property and development market.
Birchlane Furnishing has become one of the leading furniture & appliance suppliers to the property market withing London. With over 10 years experience, we have increased our business to supply not only private landlords and managing agents, but also property developers, housing associations and local councils.
We offer not only a complete range of furniture which includes beds, wardrobes, dining sets and sofas, but also a high quality, full delivery and assembly service to help you with all our furnishing needs.

Target Market(s)

Private landlords, estate agents, letting agents, property management companies

Industry/Entity Type

Business

Contact Information for Business Card

Name,
Title,
Address,
Mobile,
Telephone,
Fax, Website, email address

Font styles to use
Sans Serif

Colors
3176b5
0555a3
85abd2
cfdeed

Requirements
Must have
• All the above information for each of our staff, along with our logo

```html
<!DOCTYPE html>
<html lang="en">
<head>
<meta charset="UTF-8">
<title>Birchlane Furnishing – Business Card</title>
<link href="https://fonts.googleapis.com/css2?family=Lato:wght@400;700&display=swap" rel="stylesheet">
<style>
  :root {
    --brand-blue: #0555a3;
    --mid-blue: #3176b5;
    --light-blue: #85abd2;
    --pale-blue: #cfdeed;
    --ink: #141414;
    --paper: #ffffff;
    --backdrop: #e6e8eb;
  }
  * { margin: 0; padding: 0; box-sizing: border-box; }
  html, body { width: 1200px; height: 900px; overflow: hidden; }
  body {
    background: var(--backdrop);
    font-family: "Lato", sans-serif;
    position: relative;
  }
  .card {
    position: absolute;
    width: 600px;
    height: 343px;
    overflow: hidden;
    box-shadow: 0 6px 18px rgba(0,0,0,.18);
  }
  .brand-lockup { display: flex; align-items: center; gap: 12px; white-space: nowrap; }
  .brand-square { width: 24px; height: 24px; background: var(--paper); flex: none; }
  .brand-name, .brand-tagline, .brand-web { white-space: nowrap; }

  /* Back side */
  .card-back {
    left: 540px; top: 60px;
    background: var(--brand-blue);
    color: var(--paper);
    display: flex; flex-direction: column; align-items: center; justify-content: center;
    text-align: center;
  }
  .card-back .brand-name { font-size: 32px; letter-spacing: 1px; text-transform: uppercase; font-weight: 400; }
  .card-back .brand-tagline { font-size: 15px; letter-spacing: 1.5px; text-transform: uppercase; margin-top: 8px; }
  .card-back .brand-web { font-size: 17px; letter-spacing: 2.5px; margin-top: 34px; }

  /* Front side */
  .card-front {
    left: 60px; top: 480px;
    background: var(--paper);
    color: var(--ink);
  }
  .contact-block { position: absolute; left: 44px; top: 40px; width: 220px; }
  .person-name { font-size: 26px; font-weight: 400; white-space: nowrap; }
  .person-title { font-size: 16px; color: var(--mid-blue); margin-top: 2px; }
  .address { font-size: 15px; line-height: 1.3; margin-top: 16px; white-space: nowrap; }
  .contact-list { list-style: none; margin-top: 12px; font-size: 15px; line-height: 1.4; }
  .contact-list li { display: flex; align-items: center; gap: 8px; white-space: nowrap; }
  .contact-list svg { width: 12px; height: 12px; fill: var(--mid-blue); flex: none; }

  .front-brand {
    position: absolute; right: 34px; top: 150px;
  }
  .front-brand .brand-square { width: 20px; height: 20px; background: var(--mid-blue); }
  .front-brand .brand-name { font-size: 21px; text-transform: uppercase; letter-spacing: .5px; color: var(--ink); }
  .front-brand .brand-tagline { font-size: 11px; letter-spacing: 1px; text-transform: uppercase; margin-top: 4px; margin-left: 32px; }

  .footer-band {
    position: absolute; left: 0; right: 0; bottom: 0; height: 52px;
    background: var(--mid-blue);
  }
  .footer-band .accent {
    position: absolute; right: 0; bottom: 0; width: 300px; height: 16px;
    background: var(--light-blue);
    clip-path: polygon(6% 0, 100% 0, 100% 100%, 0 100%);
  }
  .footer-band .web {
    position: absolute; left: 44px; top: 11px;
    font-size: 16px; letter-spacing: 1px; color: var(--paper); white-space: nowrap;
  }
</style>
</head>
<body>

<section class="card card-back">
  <div class="brand-lockup">
    <span class="brand-square"></span>
    <span class="brand-name">Birchlane Furnishing</span>
  </div>
  <p class="brand-tagline">Trade Furniture Solutions</p>
  <p class="brand-web">www.trade.birchlane.co.uk</p>
</section>

<section class="card card-front">
  <div class="contact-block">
    <h1 class="person-name">Daniel Hartwell</h1>
    <p class="person-title">Manager</p>
    <p class="address">22B Millbrook Trade Estate<br>Northfield, London</p>
    <ul class="contact-list">
      <li>
        <svg viewBox="0 0 16 16" aria-hidden="true"><path d="M3.6 1.2l2.4 2.6-1.3 1.9c.9 2 2.5 3.6 4.6 4.6l1.9-1.3 2.6 2.4-1.3 2.6C7.2 13.6 2.4 8.8 1 3z"/></svg>
        020 7946 0321
      </li>
      <li>
        <svg viewBox="0 0 16 16" aria-hidden="true"><path d="M4 1h8v14H4zM5.5 2.5v9h5v-9zM7.3 12.6h1.4V14H7.3z"/></svg>
        020 7946 0000
      </li>
      <li>
        <svg viewBox="0 0 16 16" aria-hidden="true"><path d="M1 3h14v10H1zM2.5 4.3v.5L8 8.6l5.5-3.8v-.5zM2.5 6.6v5h11v-5L8 10.4z"/></svg>
        info@trade.birchlane.co.uk
      </li>
    </ul>
  </div>

  <div class="front-brand">
    <div class="brand-lockup">
      <span class="brand-square"></span>
      <span class="brand-name">Birchlane Furnishing</span>
    </div>
    <p class="brand-tagline">Trade Furniture Solutions</p>
  </div>

  <div class="footer-band">
    <span class="web">www.trade.birchlane.co.uk</span>
    <span class="accent"></span>
  </div>
</section>

</body>
</html>
```